New brand for digital company - your chance to get creative

We need to create a brand for our new business 'Lanternfish Digital'. Please read the brief below before progressing as we are looking for some quite specific outputs.

Background

We are positioning ourselves as ‘marketing technologists’ - we're helping businesses engage with their customers in the online space.

Our tactics include branding, marketing, online management, and social media, however we are differentiating ourselves by focusing on overall strategy, not just tactics. Our tagline is ‘Online made simple’.

We have stipulated some parameters for the brand but otherwise want designers to exercise their creativity.

Requirements
Must have
• We want to see an entire concept, not just a logo.

```html
<!DOCTYPE html>
<html lang="en">
<head>
<meta charset="utf-8">
<title>Lanternfish Digital — Flyer</title>
<link rel="stylesheet" href="https://fonts.googleapis.com/css2?family=Arvo:ital,wght@0,700;1,700&family=Noto+Serif:ital,wght@0,700;1,700&display=swap">
<style>
  :root {
    --backdrop: #1c1c1c;
    --paper: #ffffff;
    --orange: #ff7f0e;
    --ink: #111111;
    --shadow: rgba(0, 0, 0, 0.55);
  }
  * { margin: 0; padding: 0; box-sizing: border-box; }
  html, body {
    width: 1200px;
    height: 900px;
    overflow: hidden;
    background: var(--backdrop);
  }
  .canvas {
    position: relative;
    width: 1200px;
    height: 900px;
  }
  .flyer {
    position: absolute;
    left: 314px;
    top: 46px;
    width: 497px;
    height: 703px;
    background: var(--paper);
    overflow: hidden;
    transform: scale(1.15);
    transform-origin: top left;
    box-shadow: 0 6px 24px var(--shadow);
  }
  .brand {
    position: absolute;
    left: 25px;
    top: 22px;
    display: flex;
    align-items: center;
    gap: 7px;
  }
  .brand-mark {
    width: 12px;
    height: 12px;
    border-radius: 50%;
    background: var(--orange);
  }
  .brand-name {
    font-family: "Arvo", serif;
    font-weight: 700;
    font-size: 19px;
    line-height: 1;
    color: var(--orange);
  }
  .headline {
    position: absolute;
    right: 25px;
    top: 85px;
    font-family: "Arvo", serif;
    font-weight: 700;
    font-size: 31px;
    line-height: 1;
    color: var(--orange);
    letter-spacing: 0.5px;
  }
  .pull-quote {
    position: absolute;
    right: 25px;
    top: 120px;
    width: 320px;
    text-align: right;
    font-family: "Noto Serif", serif;
    font-style: italic;
    font-weight: 700;
    font-size: 8.2px;
    line-height: 11px;
    color: var(--ink);
  }
  .body-copy {
    position: absolute;
    left: 95px;
    top: 176px;
    width: 366px;
    font-family: "Noto Serif", serif;
    font-weight: 700;
    font-size: 9.3px;
    line-height: 14.6px;
    text-align: justify;
    text-indent: 48px;
    color: var(--ink);
  }
  .orange-band {
    position: absolute;
    left: 0;
    top: 393px;
    width: 100%;
    height: 310px;
    background: var(--orange);
  }
  .feature-visual {
    position: absolute;
    left: 150px;
    top: 440px;
    width: 347px;
    height: 240px;
    background: radial-gradient(ellipse 45% 40% at 55% 55%, rgba(40, 20, 5, 0.85) 0%, rgba(80, 35, 5, 0.45) 45%, rgba(255, 127, 14, 0) 100%);
  }
  .vertical-title {
    position: absolute;
    left: 18px;
    bottom: 22px;
    writing-mode: vertical-rl;
    transform: rotate(180deg);
    font-family: "Arvo", serif;
    font-weight: 700;
    font-size: 71px;
    line-height: 1;
    letter-spacing: 1px;
    white-space: nowrap;
  }
  .vertical-title .on-band { color: var(--paper); }
  .vertical-title .on-paper { color: var(--ink); }
</style>
</head>
<body>
<main class="canvas">
  <article class="flyer">
    <div class="orange-band"></div>

    <div class="brand">
      <span class="brand-mark"></span>
      <span class="brand-name">Lanternfish Digital</span>
    </div>

    <h1 class="headline">LOREM IPSUM</h1>
    <p class="pull-quote">„Neque porro quisquam est qui dolorem ipsum quia dolor sit amet, consectetur, adipisci velit...”</p>

    <p class="body-copy">Lorem ipsum dolor sit amet, consectetur adipiscing elit. In placerat risus nec justo placerat pharetra. Aliquam urna leo, mollis id molestie et, dictum sit amet diam. Nunc ornare risus in tortor hendrerit sagittis. Aenean malesuada, velit non viverra luctus, lacus nunc cursus tellus, vel facilisis lacus dolor a dui. Suspendisse varius dapibus elit, eget suscipit nunc laoreet ut. Vestibulum cursus elit ante. Maecenas vehicula odio lobortis tortor vulputate vehicula. Donec pretium gravida diam id convallis. Vestibulum ante ipsum primis in faucibus orci luctus et ultrices posuere cubilia Curae; Cras sit amet justo libero. Nunc urna nunc, hendrerit ut sollicitudin sit amet, mollis non ligula.</p>

    <div class="feature-visual" role="img" aria-label="Dark spiky tuft of thin black strands resting on an orange surface, casting a soft shadow"></div>

    <h2 class="vertical-title"><span class="on-band">LOREM</span> <span class="on-paper">IPSUM</span></h2>
  </article>
</main>
</body>
</html>
```